HWTC Marwood Terrace Bathroom Remodeling Postcard

We are a bathroom remodeling contractor in Los Angeles, California called Halvern Washroom Tilecraft. We want to create a postcard to send out to a specific condominium complex in the city of Burbank called Marwood Terrace. The postcard will be advertising a specific offer and should showcase our professionalism and quality of work. We have experience working in this particular housing development so we want to communicate that we are familiar with it. We want to be the first contractor that comes to mind when anyone who lives here starts thinking about a bathroom remodel in their home.

The postcard design should be an eye-catching combination of text and photos. The attached photos can be cropped if necessary. We have sent a variety of photos to choose from. Not all of the photos need to be included.

This is the specific text that should appear on the postcard:

Attn: Marwood Terrace Homeowners

2015 Bathroom Remodeling Sales Event!

Now through June 1, 2015 | Call Today for Details

Complete Custom Remodels Starting at $9999 (Labor and Materials)

14 days, Start to Finish, Fully-Permitted

Professional, Courteous, Quick & Clean!

halvernwashroomtilecraft.example

Licensed (#504318), Bonded and Insured

555-302-4917

Marwood Terrace customer references available upon request. Some restrictions apply. Ad price for bathroom with tub/shower combo, call for price on shower only bathroom. Hard costs for permits not included. Tax on finish materials not included. Call today to lock in your special savings.

```html
<!DOCTYPE html>
<html lang="en">
<head>
<meta charset="utf-8">
<title>HWTC Marwood Terrace Bathroom Remodeling Postcard</title>
<link rel="stylesheet" href="https://fonts.googleapis.com/css2?family=Roboto+Condensed:wght@400;700&family=Roboto:wght@500;700&family=Montserrat:wght@700&family=Oswald:wght@300;400&family=Lato:wght@700&display=swap">
<style>
  :root {
    --page: #1e1e1e;
    --navy: #14305f;
    --navy-deep: #0f2550;
    --blue: #1179c0;
    --blue-mid: #1a6cb0;
    --blue-text: #1a5ea0;
    --sky: #93d2f6;
    --yellow: #f5ea4a;
    --white: #ffffff;
    --tile-light: #b9b77a;
    --tile-dark: #6f7a55;
    --tile-teal: #9cc9c2;
  }
  * { margin: 0; padding: 0; box-sizing: border-box; }
  html, body { width: 1200px; height: 900px; overflow: hidden; background: var(--page); }
  .postcard {
    position: absolute; left: 124px; top: 88px;
    width: 960px; height: 744px; background: var(--white); overflow: hidden;
  }
  .postcard-shapes { position: absolute; inset: 0; }
  .text { position: absolute; white-space: nowrap; }

  .attn { left: 0; width: 372px; top: 30px; text-align: center;
    font: 700 19px/1 "Montserrat", sans-serif; color: var(--white); }
  .event-year { left: 0; width: 372px; top: 58px; text-align: center;
    font: 700 46px/1 "Roboto Condensed", sans-serif; color: var(--yellow); letter-spacing: 0.5px; }
  .event-title { left: 0; width: 372px; top: 108px; text-align: center;
    font: 500 25px/1 "Roboto", sans-serif; color: var(--white); }
  .event-dates { left: 0; width: 372px; top: 140px; text-align: center;
    font: 300 16px/1 "Oswald", sans-serif; color: var(--white); text-transform: uppercase; }

  .offer { left: 24px; top: 194px; font: 700 23px/30px "Roboto Condensed", sans-serif; color: var(--yellow); }
  .offer .price { color: var(--white); }

  .timeline { left: 24px; top: 282px; font: 700 18px/1 "Lato", sans-serif; color: var(--blue-text); }

  .promise { left: 24px; top: 340px; font: 700 57px/54px "Roboto Condensed", sans-serif;
    color: var(--sky); text-transform: uppercase; }

  .brand-name { left: 166px; top: 582px; font: 700 26px/29px "Roboto Condensed", sans-serif;
    color: var(--navy); }
  .brand-byline { left: 166px; top: 643px; font: 700 11px/1 "Roboto Condensed", sans-serif;
    color: var(--navy); letter-spacing: 0.5px; }

  .license { left: 24px; top: 698px; font: 700 16px/1 "Lato", sans-serif; color: var(--white); }

  .phone { right: 28px; top: 646px; font: 700 30px/1 "Roboto Condensed", sans-serif; color: var(--navy); }
  .website { right: 28px; top: 682px; font: 700 14px/1 "Lato", sans-serif; color: var(--blue-text); }
</style>
</head>
<body>
<main class="postcard">
  <svg class="postcard-shapes" width="960" height="744" viewBox="0 0 960 744" aria-hidden="false">
    <defs>
      <linearGradient id="body-blue" x1="0" y1="0" x2="1" y2="0">
        <stop offset="0" stop-color="#1d75b8"/>
        <stop offset="0.6" stop-color="#16498a"/>
        <stop offset="1" stop-color="#122e60"/>
      </linearGradient>
      <linearGradient id="tile-wall" x1="0" y1="0" x2="1" y2="1">
        <stop offset="0" stop-color="#9cc9c2"/>
        <stop offset="0.45" stop-color="#b9b77a"/>
        <stop offset="1" stop-color="#6f7a55"/>
      </linearGradient>
      <linearGradient id="shower-glass" x1="0" y1="0" x2="1" y2="1">
        <stop offset="0" stop-color="#d9d4c6"/>
        <stop offset="1" stop-color="#a59a82"/>
      </linearGradient>
      <linearGradient id="shower-warm" x1="0" y1="0" x2="1" y2="1">
        <stop offset="0" stop-color="#e3c9a3"/>
        <stop offset="1" stop-color="#a98a62"/>
      </linearGradient>
    </defs>

    <!-- left blue body with diagonal edge -->
    <polygon points="0,0 411,0 656,744 0,744" fill="url(#body-blue)"/>
    <!-- navy diagonal stripe -->
    <polygon points="350,0 411,0 604,586 545,586" fill="var(--navy-deep)"/>

    <!-- headline box -->
    <polygon points="0,0 346,0 410,176 0,176" fill="var(--blue)"/>
    <line x1="348" y1="0" x2="414" y2="180" stroke="var(--white)" stroke-width="5"/>
    <line x1="0" y1="180" x2="414" y2="180" stroke="var(--white)" stroke-width="5"/>

    <!-- timeline strip -->
    <polygon points="0,278 384,278 392,322 0,322" fill="#0b2148" opacity="0.55"/>
    <polygon points="0,272 378,272 390,314 0,314" fill="var(--white)"/>

    <!-- shower photograph -->
    <g role="img" aria-label="Photo of a mosaic-tiled walk-in shower with rain head and chrome fixtures">
      <polygon points="418,0 960,0 960,580 605,580" fill="url(#tile-wall)"/>
    </g>

    <!-- white logo area -->
    <polygon points="0,552 575,552 620,684 0,684" fill="var(--white)"/>

    <!-- contact panel -->
    <polygon points="600,586 960,586 960,598 604,598" fill="var(--navy)"/>
    <polygon points="609,604 960,604 960,744 656,744" fill="var(--white)"/>

    <!-- round photo frames -->
    <g>
      <circle cx="516" cy="280" r="92" fill="var(--white)"/>
      <circle cx="516" cy="280" r="84" fill="var(--navy)"/>
      <circle cx="516" cy="280" r="77" fill="var(--blue)"/>
      <circle cx="516" cy="280" r="71" fill="var(--white)"/>
      <g role="img" aria-label="Photo of a glass-enclosed shower with stone tile">
        <circle cx="516" cy="280" r="67" fill="url(#shower-glass)"/>
      </g>
    </g>
    <g>
      <circle cx="566" cy="502" r="92" fill="var(--white)"/>
      <circle cx="566" cy="502" r="84" fill="var(--navy)"/>
      <circle cx="566" cy="502" r="77" fill="var(--blue)"/>
      <circle cx="566" cy="502" r="71" fill="var(--white)"/>
      <g role="img" aria-label="Photo of a remodeled shower with warm beige tile and glass door">
        <circle cx="566" cy="502" r="67" fill="url(#shower-warm)"/>
      </g>
    </g>

    <!-- brand square -->
    <rect x="70" y="568" width="80" height="82" fill="var(--navy)"/>

    <!-- phone icon -->
    <rect x="742" y="650" width="26" height="26" rx="3" fill="var(--blue-text)"/>
    <path d="M749 655 l4 0 l1.5 5 l-2.5 2 q2 4 5 6 l2 -2.5 l5 1.5 l0 4 q-1 1.5 -3 1.5 q-13 -2 -14 -15 q0 -2 2 -2.5z" fill="var(--white)"/>

    <!-- globe icon -->
    <g fill="none" stroke="var(--blue-text)" stroke-width="1.4">
      <circle cx="686" cy="689" r="8"/>
      <ellipse cx="686" cy="689" rx="3.5" ry="8"/>
      <line x1="678" y1="689" x2="694" y2="689"/>
      <line x1="680" y1="684" x2="692" y2="684"/>
      <line x1="680" y1="694" x2="692" y2="694"/>
    </g>
  </svg>

  <p class="text attn">Attn: Marwood Terrace Homeowners</p>
  <h1 class="text event-year">2015 BATHROOM</h1>
  <p class="text event-title">Remodeling Sales Event!</p>
  <p class="text event-dates">Now through June 1, 2015 | Call Today for Details</p>

  <p class="text offer">Complete Custom Remodels Starting at<br><span class="price">$9999</span> (Labor and Materials)</p>

  <p class="text timeline">14 days, Start to Finish, Fully-Permitted</p>

  <h2 class="text promise">Professional,<br>Courteous,<br>Quick &amp; Clean!</h2>

  <p class="text brand-name">Halvern<br>Washroom Tilecraft</p>
  <p class="text brand-byline">By Fenwick &amp; Company</p>

  <p class="text license">Licensed (#504318), Bonded and Insured</p>

  <p class="text phone">5553024917</p>
  <p class="text website">halvernwashroomtilecraft.example</p>
</main>
</body>
</html>
```